Business cards - ZELTO Roofing & Siding

We need simple business cards made up for our Roofing & Siding business based in Calgary Alberta.
The logo on one side of the card and potentially our slogan "Honest Work, Built to Last".
The other side could have:
-A small logo
-Rep name:
-Rep cell phone:
-Rep email:
-Office phone: 403-688-2904
-Website: PrairieTopCrafters.com

We would like to incorporate the colours from our logo, especially the lite blue on the jpeg file. I have attached the ai file and jpeg file. We like the colours better on the jpeg file.

```html
<!DOCTYPE html>
<html lang="en">
<head>
<meta charset="utf-8">
<title>ZELTO Roofing &amp; Siding – Business Cards</title>
<link rel="stylesheet" href="https://fonts.googleapis.com/css2?family=Arimo:wght@400;700&display=swap">
<style>
  :root {
    --brand-blue: #0b62b3;
    --brand-red: #e21f26;
    --ink: #1b1b1b;
    --card-white: #f7f7f7;
    --backdrop: #e4e1de;
  }
  * { margin: 0; padding: 0; box-sizing: border-box; }
  html, body { width: 1200px; height: 960px; overflow: hidden; }
  body {
    background: var(--backdrop);
    font-family: "Arimo", Arial, sans-serif;
    color: var(--ink);
    position: relative;
  }
  .card {
    position: absolute;
    left: 285px;
    width: 630px;
    height: 360px;
    box-shadow: 0 6px 18px rgba(0,0,0,0.12);
    overflow: hidden;
  }
  .card--front { top: 90px; background: var(--brand-blue); }
  .card--back { top: 510px; background: var(--card-white); }

  .front-wordmark {
    position: absolute; inset: 0;
    display: flex; align-items: center; justify-content: center; gap: 14px;
  }
  .front-wordmark .mark-square { width: 18px; height: 18px; background: #ffffff; }
  .front-wordmark .name {
    color: #ffffff; font-size: 34px; font-weight: 700; letter-spacing: 1px;
    white-space: nowrap;
  }

  .back-wordmark {
    position: absolute; left: 34px; top: 156px;
    display: flex; align-items: center; gap: 10px;
  }
  .back-wordmark .mark-square { width: 14px; height: 14px; background: var(--brand-blue); flex: none; }
  .back-wordmark .name {
    font-size: 20px; font-weight: 700; color: var(--ink); white-space: nowrap;
  }

  .divider {
    position: absolute; left: 330px; top: 95px; width: 2px; height: 130px;
    background: var(--brand-red);
  }

  .contact { position: absolute; left: 350px; top: 85px; }
  .contact .rep-name {
    color: var(--brand-blue); font-size: 20px; font-weight: 700; text-transform: uppercase;
  }
  .contact .rep-title { font-size: 14px; margin-bottom: 10px; }
  .contact .line { display: flex; align-items: flex-start; gap: 8px; font-size: 13px; line-height: 17px; margin-bottom: 3px; }
  .contact .line svg { flex: none; margin-top: 2px; }

  .footer-stripes { position: absolute; left: 0; bottom: 0; width: 630px; height: 80px; }
  .slogan {
    position: absolute; right: 30px; bottom: 30px;
    color: #ffffff; font-size: 15px; font-weight: 700; white-space: nowrap;
  }
</style>
</head>
<body>

<section class="card card--front" aria-label="Business card front">
  <div class="front-wordmark">
    <span class="mark-square"></span>
    <span class="name">ZELTO Roofing &amp; Siding</span>
  </div>
</section>

<section class="card card--back" aria-label="Business card back">
  <div class="back-wordmark">
    <span class="mark-square"></span>
    <span class="name">ZELTO Roofing &amp; Siding</span>
  </div>

  <div class="divider"></div>

  <div class="contact">
    <p class="rep-name">Daniel Rourke</p>
    <p class="rep-title">General Manager</p>
    <div class="line">
      <svg width="12" height="14" viewBox="0 0 12 14"><path d="M6 1a4.5 4.5 0 0 0-4.5 4.5C1.5 9 6 13 6 13s4.5-4 4.5-7.5A4.5 4.5 0 0 0 6 1z" fill="none" stroke="#0b62b3" stroke-width="1.5"/><circle cx="6" cy="5.5" r="1.6" fill="#0b62b3"/></svg>
      <span>2740 - 9 Avenue S.E. Calgary<br>Alberta T2G 0T4</span>
    </div>
    <div class="line">
      <svg width="12" height="12" viewBox="0 0 12 12"><path d="M2.5 1l2 2.5-1 1.5a7 7 0 0 0 3.5 3.5l1.5-1 2.5 2-1 1.5C5 11 1 7 1 2.5z" fill="#0b62b3"/></svg>
      <span>403-688-2904</span>
    </div>
    <div class="line">
      <svg width="12" height="12" viewBox="0 0 12 12"><rect x="0.5" y="2" width="11" height="8" fill="#0b62b3"/><path d="M0.5 2.5L6 6.5l5.5-4" fill="none" stroke="#fff" stroke-width="1"/></svg>
      <span>info@PrairieTopCrafters.com</span>
    </div>
    <div class="line">
      <svg width="12" height="12" viewBox="0 0 12 12"><circle cx="6" cy="6" r="5" fill="none" stroke="#0b62b3" stroke-width="1.3"/><path d="M1 6h10M6 1c-2.5 3-2.5 7 0 10M6 1c2.5 3 2.5 7 0 10" fill="none" stroke="#0b62b3" stroke-width="1"/></svg>
      <span>www.PrairieTopCrafters.com</span>
    </div>
  </div>

  <svg class="footer-stripes" viewBox="0 0 630 80" aria-hidden="true">
    <polygon points="0,44 378,44 376,48 0,48" fill="#0b62b3"/>
    <polygon points="0,52 374,52 368,68 0,68" fill="#e21f26"/>
    <polygon points="380,20 630,10 630,58 366,70" fill="#0b62b3"/>
  </svg>
  <p class="slogan">Honest Work, Built to Last</p>
</section>

</body>
</html>
```